Create a Brochure Design for Harlow Senior Living

Harlow Senior Living is a subsidiary of the Harlow Care Group. This brochure is specifically for the Harlow Senior Living company and brand. Create a 3 panel, front and back, tri-fold brochure. This brochure will be a way to introduce our senior living care home to the community, prospective, clients, and various referral partners. It is modern and state of the art home. Like the home, the brochure must be eye catching, unique in its deliverables (as it doesn’t feel like a care facility) and demonstrate both attention to detail and comfort. Our organization is sophisticated and built around warmth, care and individualized personal attention. The most important aspect of this design is to focus on creating a nurturing, warm, and inviting feel where you would want to put your own loved ones in our care home.
I am open to the creativity of the designer to develop something based on the above criteria; however I would like the design to work well with the existing collateral material. What I mean by that is that while I want everything to have its own personality and stand out as its own brand representative, I still need to be able to tell that the overall design concept stays stylistically inside of the same ‘family’ of existing designed material. Because of this, below I would like for the designer to pull inspiration from the link to our website (Located below) as well as from the attachment of our recently refreshed business cards (Attached). This should allow each design to be unique and creative, while still staying inside of a framework and the feel/style that I am looking for.
Finally, I want all the designers to understand that this brochure design is for a facility where we are responsible to provide care for active, positive, and happy seniors/elders. We have care professionals and staff on-site to provide 24x7, around the clock, care to the elders and geriatric residents as it is needed and required. The photos that are used must represent aging gracefully and with elegance.
Target Market(s)
Seniors(50+), Caring Family Members, Social Workers, Physicians, Hospitals
Industry/Entity Type
Business
Requirements
Must have
- • The company logo must be included.
Nice to have
- Attached you will find a sampling of images related to the long term care industry. Please feel free to use your own images as you see fit. The interior care home pictures are of our actual facility and should be incorporated into the brochure and your design.
Company Information
• Look under the Harlow Senior Living tab at
www.harlowcaregroup.example.

```html
<!DOCTYPE html>
<html lang="en">
<head>
<meta charset="utf-8">
<title>Harlow Senior Living – Tri-fold Brochure, Inside Spread</title>
<link rel="stylesheet" href="https://fonts.googleapis.com/css2?family=Crimson+Text:ital,wght@0,400;0,600;1,400&display=swap">
<style>
  :root {
    --teal: #4e8b88;
    --teal-deep: #3f7a77;
    --cream: #fcf1d6;
    --cream-light: #fef7e6;
    --ink: #3a3024;
    --quote-ink: #4e8b88;
    --on-teal: #f6efdc;
    --backdrop: #4a4d50;
  }
  * { box-sizing: border-box; margin: 0; padding: 0; }
  html, body { width: 1200px; height: 800px; overflow: hidden; }
  body {
    background: var(--backdrop);
    font-family: "Crimson Text", Georgia, serif;
    color: var(--ink);
  }
  .brochure {
    position: absolute;
    left: 90px; top: 40px;
    width: 1020px; height: 720px;
    display: flex;
    box-shadow: 0 18px 40px rgba(0,0,0,.35);
  }
  .panel { position: relative; width: 340px; height: 720px; overflow: hidden; }
  .panel + .panel { border-left: 1px solid rgba(0,0,0,.06); }

  .panel--home { background: linear-gradient(180deg, var(--cream-light), var(--cream)); }
  .panel--care { background: linear-gradient(180deg, var(--cream-light), var(--cream)); }
  .panel--family { background: var(--teal); }

  .photo { position: absolute; left: 0; display: block; }

  /* Left panel */
  .home-copy { position: absolute; left: 32px; right: 28px; top: 352px; }
  .heading {
    font-weight: 400; color: var(--teal);
    font-size: 27px; line-height: 1.1; margin-bottom: 14px;
  }
  .body-text { font-size: 13.5px; line-height: 1.38; margin-bottom: 13px; }

  /* Middle panel */
  .care-top { position: absolute; left: 0; top: 0; }
  .hands-photo { position: absolute; left: 22px; top: 22px; }
  .quote {
    position: absolute; font-style: italic; font-size: 14px; line-height: 1.25;
  }
  .quote::before, .quote::after {
    font-style: normal; font-weight: 600; font-size: 46px; line-height: 0;
    position: absolute;
  }
  .quote::before { content: "\201C"; left: -30px; top: 22px; }
  .quote::after { content: "\201D"; right: -26px; bottom: -6px; }
  .quote--welcome { left: 52px; top: 148px; width: 160px; color: var(--on-teal); }
  .quote--welcome::before, .quote--welcome::after { color: var(--cream); }
  .quote--neighbours { left: 52px; top: 306px; width: 180px; color: var(--quote-ink); }
  .quote--neighbours::before, .quote--neighbours::after { color: #a9c4c0; }
  .care-copy { position: absolute; left: 30px; right: 26px; top: 410px; }
  .care-copy .heading { margin-bottom: 10px; }
  .service-text { font-size: 13.5px; line-height: 1.35; font-weight: 600; margin-bottom: 18px; }

  /* Right panel */
  .family-copy { position: absolute; left: 26px; right: 24px; top: 30px; color: var(--on-teal); }
  .family-copy .heading { color: var(--on-teal); font-size: 26px; }
  .family-copy .body-text { font-size: 12.5px; line-height: 1.35; margin-bottom: 10px; }
  .fees { position: absolute; left: 26px; right: 20px; top: 520px; color: var(--on-teal); }
  .fees .heading { color: var(--on-teal); font-size: 25px; margin-bottom: 12px; }
  .fee-columns { display: flex; gap: 16px; }
  .fee-list { list-style: none; font-size: 13px; line-height: 1.3; }
  .fee-list li { position: relative; padding-left: 13px; }
  .fee-list li::before {
    content: ""; position: absolute; left: 0; top: 6px;
    width: 7px; height: 7px; border-radius: 50%; background: var(--on-teal);
  }
</style>
</head>
<body>
<main class="brochure">

  <!-- Inside left panel -->
  <section class="panel panel--home">
    <svg class="photo" style="top:0" width="340" height="340" viewBox="0 0 340 340" role="img" aria-label="Photograph of a bright private bedroom with a made bed, dark wood furniture and a sliding door to a balcony">
      <defs>
        <linearGradient id="bedroomTone" x1="0" y1="0" x2="1" y2="1">
          <stop offset="0" stop-color="#e8d6a4"/>
          <stop offset=".55" stop-color="#c9a974"/>
          <stop offset="1" stop-color="#7a5638"/>
        </linearGradient>
      </defs>
      <path d="M0 0H340V300C250 280 150 330 0 318Z" fill="url(#bedroomTone)"/>
    </svg>
    <div class="home-copy">
      <h2 class="heading">It Is A Home.</h2>
      <p class="body-text">Harlow Senior Living Kalani Bay is a brand new state of the art home located in Kalani Bay at 48 Lantern Bay Drive in the Seabrook area.</p>
      <p class="body-text">The home features areas for activities and relaxation, with 2 large family rooms, a dining room, a kitchen, a spa room with soaking tub and hair washing sink.</p>
      <p class="body-text">Up to 22 “neighbors” enjoy this 11,000 sq feet home with 19 fully-furnished private rooms with private bathrooms. Room sizes range from 152 sq ft to 225 sq ft. Each has a flat screen television, electric bed(s), desk, chair, dressers, art work, built-in closet system with mirrored doors, independent air conditioner and ceiling fan.</p>
    </div>
  </section>

  <!-- Inside middle panel -->
  <section class="panel panel--care">
    <svg class="care-top" width="340" height="300" viewBox="0 0 340 300" aria-hidden="true">
      <path d="M0 0H340V240C250 258 160 300 60 290C35 288 15 284 0 280Z" fill="var(--teal)"/>
    </svg>
    <svg class="hands-photo" width="180" height="108" viewBox="0 0 180 108" role="img" aria-label="Photograph of an older hand held gently between two caring hands">
      <defs>
        <linearGradient id="handsTone" x1="0" y1="0" x2="1" y2="1">
          <stop offset="0" stop-color="#fbf5ee"/>
          <stop offset=".5" stop-color="#e7c2a6"/>
          <stop offset="1" stop-color="#c99173"/>
        </linearGradient>
      </defs>
      <rect width="180" height="108" fill="url(#handsTone)"/>
    </svg>
    <p class="quote quote--welcome">There comes a time for each of us when we need a helping hand and a soft place to land. Welcome home!</p>
    <p class="quote quote--neighbours">Neighbours live at our home. Not residents, not patients – we are all neighbours. We are family.</p>
    <div class="care-copy">
      <h2 class="heading">Lifestyle Support</h2>
      <p class="service-text">For neighbors who are relatively independent but might benefit from lifestyle support, with assistance as needed, medication management, access to staff 24/7, and regular nursing visits.</p>
      <h2 class="heading">Personal Care</h2>
      <p class="service-text">Daily bathing, dressing, toileting, incontinence care, grooming, assistance with ambulation, transfers, range of motion exercises, verbal cueing, medication management and feeding.</p>
    </div>
  </section>

  <!-- Inside right panel -->
  <section class="panel panel--family">
    <div class="family-copy">
      <h2 class="heading">We are family.</h2>
      <p class="body-text">Harlow Senior Living is a unique care concept, designed around a social model which encourages “neighbors” to be as independent as possible, actively participate in life here, and interact with their fellow neighbors.</p>
      <p class="body-text">Harlow Care Group is proud to usher in a new era in long term care — Harlow Senior Living.</p>
      <p class="body-text">Stay busy doing what you love here! Participate in as many activities as you like, keep up your hobbies and discover life anew.</p>
    </div>
    <svg class="photo" style="top:250px" width="340" height="260" viewBox="0 0 340 260" aria-hidden="true">
      <path d="M0 22C110 0 230 4 340 0V204C240 212 120 228 0 260Z" fill="var(--cream)"/>
    </svg>
    <svg class="photo" style="top:262px" width="340" height="236" viewBox="0 0 340 236" role="img" aria-label="Photograph of a spacious family room with sofas, soft lighting and warm wood furniture">
      <defs>
        <linearGradient id="loungeTone" x1="0" y1="0" x2="1" y2="1">
          <stop offset="0" stop-color="#f1e6cf"/>
          <stop offset=".5" stop-color="#b79773"/>
          <stop offset="1" stop-color="#6e4e38"/>
        </linearGradient>
      </defs>
      <path d="M0 20C110 0 230 4 340 0V186C240 196 120 210 0 236Z" fill="url(#loungeTone)"/>
    </svg>
    <div class="fees">
      <h2 class="heading">Monthly Fees Include</h2>
      <div class="fee-columns">
        <ul class="fee-list">
          <li>3 daily meals + snacks</li>
          <li>Activities</li>
          <li>Laundry</li>
          <li>Housekeeping</li>
          <li>Utilities</li>
        </ul>
        <ul class="fee-list">
          <li>Accommodations</li>
          <li>Medication Management</li>
          <li>Care Planning</li>
          <li>Regular Nursing Visits</li>
          <li>Access to Staff 24/7</li>
        </ul>
      </div>
    </div>
  </section>

</main>
</body>
</html>
```